Website for Dental Office - The Brightcrest Clinic

The brightcrest clinic is a dental office offering cosmetic dentistry, general dentistry, and multi-specialty dental care all under one roof in our state-of-the-art cosmetic dental center. We are particularly striving to provide services that fit the need of the young generation. Thus, we hope to have a modern, professional concise website that represents our spirit.

*Should be able to switch from English to Chinese

6 sections besides homepage:
Home, Meet us, Services,
Patient Info, Cases&Reviews, Blog, Contact

The Services sections should contain multiple subsections such as cleaning and prevention, cosmetic dentistry, implant dentistry, removable dentures, etc...
The Patient Info section is also intended to contain several subsections such as
New Patient offer, accepted Insurance, patient portal, helpful tips, etc...

Target Market(s)

young generation

Coding

Number of Pages Required

5+ page

Font styles to use
Sans Serif

Colors
0592cd
33a6d7
85cae6
00a990
33b8a4
86cfc6
cee9f5
cfeae6
3277b5

Requirements
Must have
• *Should be able to switch from English to Chinese
Nice to have
• http://www.thebrightcrestclinic-example.com/
• As a reference, the above link is the current website, but we would like to change the appearance and the content (our new logo's picture is attached)

```html
<!DOCTYPE html>
<html lang="en">
<head>
<meta charset="utf-8">
<title>The Brightcrest Clinic</title>
<link href="https://fonts.googleapis.com/css2?family=Nunito:wght@400;600;700&family=Mulish:wght@400;600&family=Oswald:wght@300;400&family=Caveat:wght@500&display=swap" rel="stylesheet">
<style>
:root{
  --blue:#29a3dc;
  --blue-deep:#0592cd;
  --blue-soft:#85cae6;
  --ice:#cee9f5;
  --navy:#3277b5;
  --green:#00a990;
  --teal:#33b8c8;
  --text:#555c60;
  --dark:#333;
  --white:#fff;
  --gold:#f4b400;
}
*{box-sizing:border-box;margin:0;padding:0}
html,body{width:1200px;height:4734px;overflow:hidden}
body{font-family:"Mulish",sans-serif;color:var(--text);background:var(--white)}
.page{position:relative;width:1200px;height:4734px;overflow:hidden}
.abs{position:absolute}
.btn{position:absolute;display:flex;align-items:center;justify-content:center;border-radius:26px;background:var(--green);color:var(--white);font:600 17px "Nunito",sans-serif;text-transform:uppercase;letter-spacing:.3px}
.heading{font:600 40px "Nunito",sans-serif;color:var(--blue);text-align:center;position:absolute;left:0;width:1200px}
.eyebrow{font:400 20px "Nunito",sans-serif;color:var(--navy);text-align:center;position:absolute;left:0;width:1200px;text-transform:uppercase}
.photo{position:absolute}

/* top bar */
.topbar{position:absolute;left:0;top:0;width:1200px;height:40px;background:var(--blue)}
.topbar .phone{position:absolute;left:80px;top:9px;color:var(--white);font:600 17px "Nunito",sans-serif;display:flex;align-items:center;gap:12px}
.topbar .lang{position:absolute;left:851px;top:11px;color:var(--white);font:600 14px "Nunito",sans-serif}
.topbar .book{position:absolute;left:904px;top:0;width:219px;height:52px;background:var(--green);color:var(--white);font:600 16px "Nunito",sans-serif;display:flex;align-items:center;justify-content:center;border-radius:0 0 6px 6px;z-index:3}

/* nav */
.nav{position:absolute;left:0;top:40px;width:1200px;height:89px;background:var(--white)}
.brand{position:absolute;display:flex;align-items:center;gap:14px}
.brand .mark{width:46px;height:46px;background:var(--blue-soft);border-radius:4px}
.brand .name{font:700 22px/1.05 "Nunito",sans-serif;color:var(--blue);text-transform:uppercase}
.menu{position:absolute;top:44px;font:600 14px "Nunito",sans-serif;color:var(--dark);text-transform:uppercase}
.menu.active{color:var(--blue)}
.menu.active::after{content:"";position:absolute;left:10px;right:10px;bottom:-10px;height:2px;background:var(--blue)}

/* hero */
.hero-photo{left:0;top:129px;width:1200px;height:560px;background:linear-gradient(90deg,#f1efed 0%,#ebe6e2 40%,#d9b8a2 62%,#b9785a 80%,#8a4b33 100%)}
.hero-tag{left:81px;top:266px;font:500 38px "Caveat",cursive;color:#444}
.hero-title{left:78px;top:312px;font:300 60px "Oswald",sans-serif;color:var(--blue);letter-spacing:-.5px}
.hero-arrow{position:absolute;top:333px;width:50px;height:50px;border:1.5px solid #777;border-radius:50%}

/* welcome */
.welcome-photo{left:125px;top:770px;width:416px;height:416px;border-radius:50%;background:radial-gradient(circle at 55% 45%,#f4d7c6,#d9b09b 55%,#9fb9c8)}
.welcome-kicker{left:608px;top:770px;font:400 21px "Nunito",sans-serif;color:var(--navy)}
.welcome-title{left:607px;top:800px;font:600 42px "Nunito",sans-serif;color:var(--blue)}
.copy{position:absolute;font-size:13.5px;line-height:27px;color:var(--text)}

/* services */
.card{position:absolute;width:311px;height:311px;background:var(--white);border-radius:4px}
.card .img{position:absolute;left:11px;top:11px;width:289px;height:217px}
.card h3{position:absolute;left:11px;top:250px;font:600 17px "Nunito",sans-serif;color:var(--blue)}
.card p{position:absolute;left:11px;top:276px;font-size:12.5px;color:var(--dark)}

/* reviews */
.avatar{left:542px;top:2429px;width:114px;height:114px;border-radius:50%;border:3px solid var(--blue);background:radial-gradient(circle,#7a4a35,#3d2418 70%,#fff 72%)}
.quote{left:240px;top:2564px;width:720px;text-align:center;font-size:14px;line-height:27px;color:var(--text)}
.quote b{color:var(--green);font:700 22px "Nunito",sans-serif;vertical-align:-4px}
.chev{position:absolute;top:2533px;width:22px;height:36px}

/* appointment */
.appt{left:141px;top:2812px;width:918px;height:364px;background:var(--blue);border-radius:50px}
.field{position:absolute;height:42px;border-radius:21px;background:var(--white);font-size:12px;color:#888;padding:14px 22px}

/* patient info */
.patient-photo{left:0;top:3194px;width:533px;height:426px;background:linear-gradient(120deg,#6fd3b3 0%,#9edccb 45%,#ecd3da 100%)}
.tab{position:absolute;top:3635px;height:72px;border-radius:36px;color:var(--white);font:600 18px "Nunito",sans-serif;display:flex;align-items:center;justify-content:center;text-transform:uppercase}

/* blog */
.post{position:absolute;width:324px;top:3848px;height:402px;border-bottom:1px solid #d6d6d6}
.post .img{position:absolute;left:0;top:0;width:324px;height:208px}
.post .date{position:absolute;left:0;top:0;width:66px;height:81px;background:var(--green);color:var(--white);text-align:center;font:600 30px/1 "Nunito",sans-serif;padding-top:16px}
.post .date span{display:block;font-size:15px;margin-top:4px;font-weight:400}
.post h3{position:absolute;left:0;top:234px;width:324px;font:400 16.5px/28px "Nunito",sans-serif;color:var(--blue)}
.post p{position:absolute;left:0;top:302px;width:324px;font-size:13px;line-height:26px;color:var(--text)}

/* footer */
.footer{left:0;top:4319px;width:1200px;height:352px;background:var(--blue)}
.foot-h{position:absolute;top:4350px;font:600 18px "Nunito",sans-serif;color:var(--white);text-transform:uppercase}
.foot-list{position:absolute;list-style:none;font-size:13.5px;color:var(--white)}
.foot-list li{height:33.5px;position:relative;padding-left:26px}
.foot-list.dots li::before{content:"";position:absolute;left:0;top:6px;width:7px;height:7px;border-radius:50%;background:var(--white)}
.foot-list.hours li{height:35.5px;padding-left:30px}
.foot-list.hours li::before{content:"";position:absolute;left:0;top:2px;width:14px;height:14px;border:2px solid var(--white);border-radius:50%}
.contact-row{position:absolute;left:610px;display:flex;gap:18px;font-size:13.5px;color:var(--white);line-height:27px}
.social{position:absolute;top:4583px;width:40px;height:40px;border:2px solid var(--white);border-radius:50%}
.bottom{left:0;top:4671px;width:1200px;height:63px;background:var(--navy);color:var(--white);font-size:13.5px;display:flex;align-items:center;justify-content:center}
</style>
</head>
<body>
<div class="page">

<header>
  <div class="topbar">
    <div class="phone">
      <svg width="22" height="22" viewBox="0 0 22 22"><circle cx="11" cy="11" r="11" fill="#fff"/><path d="M7 6c1-1 2 0 2.5 1.5s-.5 2-.5 2 1 2 3 3c0 0 .8-1 2-.5S15 14 14.5 15c-1 1.5-4 .5-6-1.5S6 7 7 6z" fill="#29a3dc"/></svg>
      555.210.4470
    </div>
    <div class="lang">EN <svg width="12" height="8" viewBox="0 0 12 8" style="margin-left:6px"><path d="M0 0h12L6 8z" fill="#fff"/></svg></div>
    <div class="book">BOOK APPOINTMENT</div>
  </div>
  <nav class="nav">
    <div class="brand" style="left:79px;top:20px">
      <div class="mark"></div>
      <div class="name">The Brightcrest<br>Clinic</div>
    </div>
    <span class="menu active" style="left:419px">Home</span>
    <span class="menu" style="left:491px">Meet Us</span>
    <span class="menu" style="left:577px">Services</span>
    <span class="menu" style="left:674px">Patient Info</span>
    <span class="menu" style="left:799px">Cases&amp;Reviews</span>
    <span class="menu" style="left:948px">Blog</span>
    <span class="menu" style="left:1013px">Contact</span>
    <svg class="abs" style="left:1107px;top:45px" width="14" height="14" viewBox="0 0 14 14"><circle cx="6" cy="6" r="4.5" stroke="#333" stroke-width="2" fill="none"/><path d="M9.5 9.5L13 13" stroke="#333" stroke-width="2"/></svg>
  </nav>
</header>

<section class="hero">
  <div class="photo hero-photo" role="img" aria-label="Smiling young woman resting her chin on her hands in a bright dental office"></div>
  <div class="abs hero-tag">"Your Smile.Our Passion"</div>
  <h1 class="abs hero-title">PROFESSIONAL EXCELLENCE</h1>
  <div class="btn" style="left:77px;top:399px;width:250px;height:48px">Request Appointment</div>
  <div class="hero-arrow" style="left:12px"><svg width="47" height="47" viewBox="0 0 47 47"><path d="M27 15l-8 8.5 8 8.5" stroke="#555" stroke-width="1.5" fill="none"/></svg></div>
  <div class="hero-arrow" style="left:1138px"><svg width="47" height="47" viewBox="0 0 47 47"><path d="M20 15l8 8.5-8 8.5" stroke="#555" stroke-width="1.5" fill="none"/></svg></div>
  <svg class="abs" style="left:0;top:560px" width="1200" height="130" viewBox="0 0 1200 130">
    <path d="M0 110 C60 70 120 40 220 40 C330 40 380 100 470 110 C560 120 600 60 700 55 C800 50 840 110 930 110 C1020 110 1080 20 1200 40 L1200 130 L0 130Z" fill="#fff"/>
    <path d="M0 110 C60 70 120 40 220 40 C330 40 380 100 470 110 C560 120 600 60 700 55 C800 50 840 110 930 110 C1020 110 1080 20 1200 40" fill="none" stroke="#29a3dc" stroke-width="4"/>
  </svg>
</section>

<section class="welcome">
  <div class="photo welcome-photo" role="img" aria-label="Close-up of a smile beside a tooth shade guide held by a gloved hand"></div>
  <div class="abs welcome-kicker">WELCOME TO</div>
  <h2 class="abs welcome-title">The Brightcrest Clinic</h2>
  <p class="copy" style="left:616px;top:864px;width:470px">Welcome to The Brightcrest Clinic where we specialize in General and Cosmetic Dentistry, Dental Implants, Periodontics (Gum Surgery), Endodontics (Root Canal Treatment) and Reconstructive Dentistry for patients in Boston, Brookline, Cambridge, Brighton, Allston, Newton, Watertown, Wellesley and all other surrounding neighborhoods of Boston, Massachusetts.</p>
  <p class="copy" style="left:616px;top:1045px;width:470px">Our specialist are also trained in providing Neurotox and Dermal Fillers and we would be honored to have you a part of our growing family.</p>
  <div class="btn" style="left:614px;top:1150px;width:176px;height:52px">Learn More</div>
</section>

<section class="services">
  <svg class="abs" style="left:0;top:1225px" width="1200" height="1035" viewBox="0 0 1200 1035">
    <path d="M0 0 C300 40 900 40 1200 0 L1200 1035 L0 1035Z" fill="#cee9f5"/>
  </svg>
  <div class="eyebrow" style="top:1353px">What We Do</div>
  <h2 class="heading" style="top:1385px">Service We Provide You</h2>

  <article class="card" style="left:110px;top:1470px"><div class="img" role="img" aria-label="Young woman smiling during a dental check-up" style="background:linear-gradient(135deg,#8fb5d8,#e2c1ad)"></div><h3>Cleaning And Prevention</h3><p>Lorem Ipsum is simply dummy</p></article>
  <article class="card" style="left:445px;top:1470px"><div class="img" role="img" aria-label="Bright smile beside a tooth shade guide" style="background:linear-gradient(135deg,#f1ece8,#c8c8c8)"></div><h3>Cosmetic Dentistry</h3><p>Lorem Ipsum is simply dummy</p></article>
  <article class="card" style="left:777px;top:1470px"><div class="img" role="img" aria-label="Smiling woman holding a dental implant model" style="background:linear-gradient(135deg,#8ec6ea,#f0e1d8)"></div><h3>Implant Dentistry</h3><p>Lorem Ipsum is simply dummy</p></article>
  <article class="card" style="left:110px;top:1803px"><div class="img" role="img" aria-label="Gloved hand holding a removable denture" style="background:linear-gradient(135deg,#9ed0ee,#2e3a4e)"></div><h3>Removable Dentures</h3><p>Lorem Ipsum is simply dummy</p></article>
  <article class="card" style="left:445px;top:1803px"><div class="img" role="img" aria-label="Girl in a dental chair receiving orthodontic care" style="background:linear-gradient(135deg,#eadfd8,#6fa9d8)"></div><h3>Orthodontic</h3><p>Lorem Ipsum is simply dummy</p></article>
  <article class="card" style="left:777px;top:1803px"><div class="img" role="img" aria-label="Smiling woman holding a clear aligner" style="background:linear-gradient(135deg,#f3ece7,#c9a58e)"></div><h3>ClearAlign</h3><p>Lorem Ipsum is simply dummy</p></article>

  <div class="btn" style="left:511px;top:2145px;width:176px;height:49px">Learn More</div>
</section>

<section class="reviews">
  <div class="eyebrow" style="top:2316px">Reviews</div>
  <h2 class="heading" style="top:2346px">Our Happy Patient</h2>
  <div class="photo avatar" role="img" aria-label="Portrait of a smiling patient"></div>
  <svg class="chev" style="left:112px" viewBox="0 0 22 36"><path d="M20 2L4 18l16 16" stroke="#bbb" stroke-width="2" fill="none"/></svg>
  <svg class="chev" style="left:1070px" viewBox="0 0 22 36"><path d="M2 2l16 16L2 34" stroke="#bbb" stroke-width="2" fill="none"/></svg>
  <p class="abs quote"><b>&ldquo;</b> I LOVE everyone at this office!! Dr. Halvorsen is the best of the best. The office staff are always courteous and kind, even kept an eye on my granddaughter who was watching TV while I was being seen. They are professional, nice, outgoing, friendly--just what every office strives to be--they have it all!! <b>&rdquo;</b></p>
  <svg class="abs" style="left:538px;top:2695px" width="124" height="22" viewBox="0 0 124 22">
    <g fill="#f4b400">
      <path id="st" d="M11 1l3 6.5 7 .8-5.2 4.8 1.4 7L11 16.6 4.8 20l1.4-7L1 8.3l7-.8z"/>
      <use href="#st" x="25"/><use href="#st" x="50"/><use href="#st" x="75"/><use href="#st" x="100"/>
    </g>
  </svg>
  <div class="abs" style="left:0;width:1200px;top:2727px;text-align:center;font:600 17px 'Nunito',sans-serif;color:var(--green)">Marla Quinby</div>
</section>

<section class="patient">
  <div class="abs" style="left:0;top:2995px;width:1200px;height:675px;background:var(--ice)"></div>
  <div class="abs appt"></div>
  <div class="abs" style="left:187px;top:2928px;font:400 20px 'Nunito',sans-serif;color:var(--white)">REQUEST YOUR</div>
  <h2 class="abs" style="left:186px;top:2960px;font:400 42px 'Nunito',sans-serif;color:var(--white)">APPOINTMENT</h2>
  <div class="field" style="left:513px;top:2865px;width:237px">Name *</div>
  <div class="field" style="left:763px;top:2865px;width:239px">Date *</div>
  <div class="field" style="left:513px;top:2922px;width:237px">Time *</div>
  <div class="field" style="left:763px;top:2922px;width:239px">Appointment For *
    <svg class="abs" style="right:16px;top:18px" width="10" height="6" viewBox="0 0 10 6"><path d="M0 0h10L5 6z" fill="#29a3dc"/></svg></div>
  <div class="field" style="left:513px;top:2981px;width:489px;height:82px;border-radius:18px">Comments and Questions *</div>
  <div class="btn" style="left:513px;top:3074px;width:128px;height:52px;font-size:18px">Submit</div>

  <div class="photo patient-photo" role="img" aria-label="Gloved hands holding a clear dental aligner"></div>
  <h2 class="abs" style="left:632px;top:3262px;font:600 42px 'Nunito',sans-serif;color:var(--blue)">Patient Info</h2>
  <p class="copy" style="left:632px;top:3320px;width:450px">With Ashgrove and Millbrook credentials that inspire confidence, we offer cosmetic dentistry, general dentistry and multi-specialty dental care all under one roof in our state-of-the-art cosmetic dental center conveniently located near Maple Square on Linden Avenue steps from City Transit.</p>
  <div class="btn" style="left:628px;top:3479px;width:177px;height:49px">Learn More</div>

  <div class="tab" style="left:77px;width:256px;background:var(--blue)">New Patient Offer</div>
  <div class="tab" style="left:342px;width:253px;background:var(--navy)">Accepted Insurance</div>
  <div class="tab" style="left:605px;width:253px;background:var(--green)">Patient Portal</div>
  <div class="tab" style="left:867px;width:256px;background:var(--teal)">Helpful Tips</div>
</section>

<section class="blog">
  <h2 class="heading" style="top:3770px">Latest Blog Post</h2>
  <article class="post" style="left:88px"><div class="img" role="img" aria-label="Smiling young woman flossing her teeth" style="background:linear-gradient(135deg,#c9a48c,#6b4536 50%,#e7e5e6)"></div><div class="date">10<span>Aug</span></div><h3>Lorem Ipsum is simply dummy text of the printing and typesetting</h3><p>Lorem Ipsum is simply dummy text of the and typesetting industry. Lorem Ipsum has been the industry's standard dummy .</p></article>
  <article class="post" style="left:437px"><div class="img" role="img" aria-label="Mother and child smiling together" style="background:linear-gradient(135deg,#a9c1e6,#7a5040 55%,#b6cf7a)"></div><div class="date">10<span>Aug</span></div><h3>Lorem Ipsum is simply dummy text of the printing and typesetting</h3><p>Lorem Ipsum is simply dummy text of the and typesetting industry. Lorem Ipsum has been the industry's standard dummy .</p></article>
  <article class="post" style="left:787px"><div class="img" role="img" aria-label="Gloved hand examining a patient's smile" style="background:linear-gradient(135deg,#e6e2de,#8a7ec4 40%,#e8c4ad)"></div><div class="date">10<span>Aug</span></div><h3>Lorem Ipsum is simply dummy text of the printing and typesetting</h3><p>Lorem Ipsum is simply dummy text of the and typesetting industry. Lorem Ipsum has been the industry's standard dummy .</p></article>
</section>

<footer>
  <div class="abs footer"></div>
  <div class="brand" style="left:83px;top:4435px">
    <div class="mark" style="background:var(--white)"></div>
    <div class="name" style="color:var(--white);font-size:19px">The Brightcrest<br>Clinic</div>
  </div>
  <div class="btn" style="left:75px;top:4502px;width:248px;height:50px;font-size:16px">Request Appointment</div>

  <h4 class="foot-h" style="left:340px">Sitemap</h4>
  <ul class="foot-list dots" style="left:340px;top:4398px">
    <li>Home</li><li>Meet Us</li><li>Services</li><li>Patient Info</li><li>Cases&amp;Reviews</li><li>Blog</li><li>Contact</li>
  </ul>

  <h4 class="foot-h" style="left:610px">Contact Us</h4>
  <div class="contact-row" style="top:4392px"><svg width="16" height="22" viewBox="0 0 16 22"><path d="M8 0a8 8 0 0 1 8 8c0 6-8 14-8 14S0 14 0 8a8 8 0 0 1 8-8z" fill="#fff"/><circle cx="8" cy="8" r="3" fill="#29a3dc"/></svg><span>270 Linden Avenue, Suite<br>12, Fairmont MA 02999</span></div>
  <div class="contact-row" style="top:4464px"><svg width="18" height="18" viewBox="0 0 18 18" style="margin-top:4px"><path d="M3 1c1.5-1 3 0 3.5 2s-.8 3-.8 3 1.5 3 4.5 4.5c0 0 1-1.2 3-.8s3 2 2 3.5c-1.5 2-6 1-9-2S1.5 2 3 1z" fill="#fff"/></svg><span>1.555.210.4470</span></div>
  <div class="contact-row" style="top:4499px"><svg width="18" height="18" viewBox="0 0 18 18" style="margin-top:4px"><rect x="1" y="5" width="16" height="11" rx="2" fill="#fff"/><rect x="5" y="1" width="8" height="5" fill="#fff"/><rect x="4" y="9" width="10" height="4" fill="#29a3dc"/></svg><span>1.555.210.4471</span></div>
  <div class="contact-row" style="top:4536px"><svg width="18" height="14" viewBox="0 0 18 14" style="margin-top:6px"><rect width="18" height="14" rx="1" fill="#fff"/><path d="M1 1l8 6 8-6" stroke="#29a3dc" stroke-width="1.5" fill="none"/></svg><span style="font-size:12.5px">hello@brightcrest-example.com</span></div>
  <div class="social" style="left:607px"></div>
  <div class="social" style="left:656px"></div>
  <div class="social" style="left:706px"></div>
  <div class="social" style="left:756px"></div>

  <h4 class="foot-h" style="left:875px">Opening Hours</h4>
  <ul class="foot-list hours" style="left:872px;top:4396px">
    <li>Sunday : Closed</li><li>Monday : Cosed</li><li>Tuesday : 9:30am - 5:00pm</li><li>Wednesday : Closed</li><li>Thursday : 9:00am - 5:00pm</li><li>Friday : 9:00am - 5:00pm</li><li>Saturday : 9:00am - 5:00pm</li>
  </ul>

  <div class="abs bottom">©THE BRIGHTCREST CLINIC - 2019 All rights reserved.</div>
</footer>

</div>
</body>
</html>
```